Acupuncture Medspa needs a business card design

I need a business card design that looks professional, has a spa-like quality and can offer a promo on the back. Initial promo is "First session free". The tagline of PinaVell is: Unwind, Mend, Glow.

PinaVell is a membership-based acupuncture medspa that offers acupuncture, cupping, and herbal therapies. Members choose between the "Refresh" membership which is for stress relief, or "Restore" which is for treating health conditions, and lastly "Rejuvenate" which is for natural facial enhancement.

Industry/Entity Type

Health And Wellness

Contact Information for Business Card

Doris Kettle, MAC, L.Ac.
614-385-2097
www.pinavell-example.com

Font styles to use
Serif
Sans Serif

Colors

Designer to choose colors to be used in the design.

Requirements
Must have
• The project must have PinaVell logo, promo on the back, and contact information
Nice to have
• I would like to see the colors of the logo used.

```html
<!DOCTYPE html>
<html lang="en">
<head>
<meta charset="utf-8">
<title>PinaVell Business Card</title>
<link rel="stylesheet" href="https://fonts.googleapis.com/css2?family=Montserrat:wght@400;500&family=Open+Sans:wght@400;700&display=swap">
<style>
  :root {
    --teal: #168b81;
    --teal-deep: #0f776e;
    --white: #ffffff;
    --paper: #e9eeee;
    --ink: #2d1a12;
  }
  * { box-sizing: border-box; margin: 0; padding: 0; }
  html, body { width: 1200px; height: 900px; overflow: hidden; }
  body {
    background: var(--paper);
    display: flex;
    flex-direction: column;
    align-items: center;
    justify-content: center;
    gap: 40px;
    font-family: "Open Sans", sans-serif;
  }
  .card {
    position: relative;
    width: 660px;
    height: 377px;
    box-shadow: 0 6px 20px rgba(0,0,0,0.12);
    overflow: hidden;
  }
  .wordmark {
    display: flex;
    align-items: center;
    gap: 14px;
    font-family: "Montserrat", sans-serif;
    font-weight: 500;
    letter-spacing: 0.06em;
    text-transform: uppercase;
  }
  .wordmark-dot {
    border-radius: 50%;
    border: 3px solid currentColor;
  }

  /* Front */
  .card-front {
    background: linear-gradient(135deg, var(--teal) 0%, var(--teal-deep) 100%);
    color: var(--white);
  }
  .card-front .wordmark {
    position: absolute;
    top: 92px;
    left: 0; right: 0;
    justify-content: center;
    font-size: 62px;
  }
  .card-front .wordmark-dot { width: 62px; height: 62px; }
  .promo {
    position: absolute;
    top: 190px;
    left: 0; right: 0;
    text-align: center;
    font-family: "Montserrat", sans-serif;
    font-size: 19px;
    letter-spacing: 0.08em;
  }
  .membership-rule {
    position: absolute;
    top: 258px;
    left: 50px; right: 50px;
    height: 1px;
    background: var(--white);
  }
  .memberships {
    position: absolute;
    top: 276px;
    left: 50px; right: 50px;
    display: flex;
    justify-content: space-between;
    font-family: "Montserrat", sans-serif;
    font-size: 16px;
    letter-spacing: 0.08em;
  }

  /* Back */
  .card-back { background: var(--white); }
  .card-back .wordmark {
    position: absolute;
    top: 52px;
    left: 48px;
    color: var(--teal);
    font-size: 40px;
  }
  .card-back .wordmark-dot { width: 40px; height: 40px; }
  .contact {
    position: absolute;
    top: 148px;
    right: 44px;
    display: flex;
    align-items: center;
    gap: 18px;
  }
  .person { text-align: right; }
  .person-name { font-weight: 700; font-size: 23px; color: var(--ink); }
  .person-credentials { font-size: 17px; color: var(--teal); }
  .contact-divider { width: 1.5px; height: 78px; background: var(--teal); }
  .contact-lines { list-style: none; font-size: 15px; color: var(--ink); line-height: 1.6; }
  .contact-lines b { color: var(--teal); font-weight: 700; margin-right: 6px; }
  .address-band {
    position: absolute;
    left: 0; right: 0;
    bottom: 44px;
    height: 44px;
    background: var(--teal);
    color: var(--white);
    font-size: 15px;
    display: flex;
    align-items: center;
    justify-content: flex-end;
    padding-right: 44px;
  }
  .edge-band {
    position: absolute;
    left: 0; right: 0;
    bottom: 0;
    height: 22px;
    background: var(--teal);
  }
</style>
</head>
<body>
  <section class="card card-front" aria-label="Card front">
    <div class="wordmark"><span class="wordmark-dot"></span>PinaVell</div>
    <p class="promo">FIRST SESSION FREE</p>
    <div class="membership-rule"></div>
    <div class="memberships">
      <span>REFRESH</span>
      <span>RESTORE</span>
      <span>REJUVENATE</span>
    </div>
  </section>

  <section class="card card-back" aria-label="Card back">
    <div class="wordmark"><span class="wordmark-dot"></span>PinaVell</div>
    <div class="contact">
      <div class="person">
        <p class="person-name">Doris Kettle</p>
        <p class="person-credentials">MAC, L.AC</p>
      </div>
      <div class="contact-divider"></div>
      <ul class="contact-lines">
        <li><b>T:</b>614-385-2097</li>
        <li><b>E:</b>info@pinavell-example.com</li>
        <li><b>W:</b>www.pinavell-example.com</li>
      </ul>
    </div>
    <div class="address-band">2740 Alder Row, Westbrook, OH 43120</div>
    <div class="edge-band"></div>
  </section>
</body>
</html>
```